New Fernleaf Skin Care company needs logo and label design for a new skin serum product

We need a name, logo, and label design for a new company that is producing an all in one all natural highly effective skin serum. The end result should include image imposed on clear 120z plastic bottle

We would like to see designs that promote an authentic, all natural, highly effective brand image. We need the product to standout amongst the crowded store shelves. The target customer includes Greenmarrow, Corvin Hale, and other upscale supermarket and drug store chains. This is an all in one skin product that aims to simplify a very crowded field and over cluttered market segment.

Reason: Need some great designs. Something very unique that stands out on the crowded store shelves.

Target Market(s)

men and woman, 25 years and older, who are healthy and care about their skin appearance

Industry/Entity Type

Plastic

Requirements
Nice to have
• I was inspired by a juice company called Meadowpressjuice.example Please check it out for inspiration.

I am also inspired by mrtalvik.example but am looking for more modern approach

I am interested in seeing the ingredients and benefits listed somewhere on the bottle. Here are some of them:

Jojoba Oil-moisturizing and soothing
Vitamin A-Anti Aging, Reduces wrinkles
Vitamin B-Anti Inflammatory
Vitamin C-Promote Collagen
Vitamin D3-Helps skin conditions
Vitamin E-Antioxidant
Squalene-Natural Moisturizing
Calsium Gluconate-Anti-Microbial
Acai-
Aloe-
Japanese Green Tea-anti-inflammatory
Glycerin-Moisturizing

```html
<!DOCTYPE html>
<html lang="en">
<head>
<meta charset="utf-8">
<title>Fernleaf Skin Care – Serum Label</title>
<link href="https://fonts.googleapis.com/css2?family=Signika:wght@400;600&display=swap" rel="stylesheet">
<style>
  :root {
    --paper: #ffffff;
    --edge: #8a8a8a;
    --leaf: #18d018;
    --brand: #14c214;
    --panel-dark: #07a007;
    --panel-light: #0fc80f;
    --sprig: #3fd43f;
    --ink-light: #ffffff;
  }
  * { margin: 0; padding: 0; box-sizing: border-box; }
  html, body {
    width: 755px; height: 1200px; overflow: hidden;
    background: var(--paper);
  }
  .canvas {
    position: relative; width: 755px; height: 1200px;
    background: var(--paper);
    border-left: 1px solid var(--edge);
    font-family: "Signika", "Trebuchet MS", sans-serif;
  }
  .label-frame {
    position: absolute; left: 219px; top: 96px;
    width: 346px; height: 770px;
    border: 3px solid var(--leaf);
    border-radius: 10px;
  }
  .brand-dot {
    position: absolute; left: 243px; top: 470px;
    width: 92px; height: 92px; border-radius: 50%;
    background: var(--brand);
  }
  .brand-name {
    position: absolute; left: 342px; top: 498px;
    color: var(--brand); font-weight: 600;
    font-size: 44px; line-height: 38px;
    white-space: nowrap;
  }
  .brand-name span { display: block; }
  .brand-name .line-two { padding-left: 6px; }
  .sprig-border {
    position: absolute; left: 222px; top: 826px;
    width: 344px; height: 30px;
    background: linear-gradient(to bottom, rgba(63,212,63,0) 0%, var(--sprig) 100%);
  }
  .ingredients-panel {
    position: absolute; left: 207px; top: 855px;
    width: 369px; height: 283px;
    border-radius: 8px;
    background: linear-gradient(160deg, var(--panel-dark) 0%, var(--panel-light) 70%, var(--panel-dark) 100%);
    padding: 11px 0 0 17px;
  }
  .ingredient-list { list-style: none; }
  .ingredient-list li {
    color: var(--ink-light); font-weight: 600;
    font-size: 17.2px; line-height: 21.6px;
    white-space: nowrap;
  }
</style>
</head>
<body>
  <main class="canvas">
    <div class="label-frame"></div>

    <div class="brand-dot"></div>
    <h1 class="brand-name">
      <span class="line-one">Fernleaf</span>
      <span class="line-two">Skin Care</span>
    </h1>

    <div class="sprig-border" role="img" aria-label="Row of small green leaf sprigs along the top of the ingredients panel"></div>

    <section class="ingredients-panel">
      <ul class="ingredient-list">
        <li>Jojoba Oil-moisturizing and soothing</li>
        <li>Vitamin A-Anti Aging, Reduces wrinkles</li>
        <li>Vitamin B-Anti Inflammatory</li>
        <li>Vitamin C-Promote Collagen</li>
        <li>Vitamin D3-Helps skin conditions</li>
        <li>Vitamin E-Antioxidant</li>
        <li>Squalene-Natural Moisturizing</li>
        <li>Calsium Gluconate-Anti-Microbial</li>
        <li>Acai-</li>
        <li>Aloe-</li>
        <li>Japanese Green Tea-anti-inflammatory</li>
        <li>Glycerin-Moisturizing</li>
      </ul>
    </section>
  </main>
</body>
</html>
```